Tobias Wrenfield - Cinematographer

NEED:
I'm looking for a sleek, professional, modern business card that will give give the recipient the impression that they can trust their production will go smoothly by hiring me. I will bring creativity and knowledge to their shoot, so that we can create powerful images.
I am looking for a card with a strong style and design ethos that could be expanded to a website and a full visual/graphic/design entity for me.
ABOUT ME:
I am a mid-twenties cinematographer, I work on music video, narrative short, commercial, and corporate projects. I blend the science and artistry of cameras and filmmaking to tell a story. I'm an artist, a technician, and a manager.
DESIGN:
I like sleek, simple design. Black, dark grays, white, dark navy, steel blues, I love cyan, but also cyan and red. I am not a fan of earthy tones. I generally prefer modern, san-serif fonts over serifs. My old logo was based on an aperture, a multi-blade device at the back of a lens that controls how much light passes through, but I made it with so many colors, that it doesn't necessarily lend itself to a specific color-scheme or design ethos. I liked that the aperture design provided a sense of the technical requirements of my job. I'm a fan of matte business cards, but am open to plenty of specialty print processes to make an outstanding card.
ATTACHED FILES:
My Old Rainbox Aperture Logo, plus a few designs I've tried playing around with, but am not tied to. I AM OPEN TO NEW DESIGNS, DO NOT FEEL TIED TO THIS.
**I've pulled my old logo down from the attached files, and instead attached other business cards I like, so as not to mislead you where I would like to go.
INFO:
Name: Tobias Wrenfield
Job: Cinematographer
Email: tkwrenfield@quillbox.example
Phone: 503.618.2907
Website: tobiaswrenfield.example
Updates
I'm adding some images of other cards that I like, and removing my old logo, since I'm looking for something new, and don't want that old logo to push anyone a certain direction.

```html
<!DOCTYPE html>
<html lang="en">
<head>
<meta charset="utf-8">
<title>Tobias Wrenfield — Cinematographer Card</title>
<link href="https://fonts.googleapis.com/css2?family=Quicksand:wght@400;500;700&family=Josefin+Sans:wght@300;400&display=swap" rel="stylesheet">
<style>
  :root {
    --backdrop: #e7e4df;
    --ink-panel: #221b22;
    --divider: #3b3e46;
    --name-teal: #3f8a8c;
    --role-grey: #8c878c;
    --detail-tan: #c9b89c;
    --mark-tan: #b6a488;
    --accent-red: #e8553a;
    --icon-ink: #221b22;
    --photo-green-deep: #16241f;
    --photo-green: #26392f;
    --photo-pale: #7d8580;
    --sky-pale: #a9d6cf;
    --city-grey: #6d6f72;
  }
  * { margin: 0; padding: 0; box-sizing: border-box; }
  html, body {
    width: 1200px; height: 877px; overflow: hidden;
    background: var(--backdrop);
  }
  .stage { position: relative; width: 1200px; height: 877px; }
  .card-sheet {
    position: absolute; left: 207px; top: 111px;
    width: 764px; height: 636px;
    transform: scale(1.03); transform-origin: 0 0;
    background: var(--divider);
  }
  .panel { position: absolute; }
  .card-back { left: 0; top: 0; width: 382px; height: 474px; background: var(--ink-panel); }
  .hero-photo {
    left: 382px; top: 0; width: 382px; height: 478px;
    background: linear-gradient(170deg, var(--photo-green) 0%, var(--photo-pale) 45%, var(--photo-green-deep) 100%);
  }
  .skyline-photo {
    left: 0; top: 480px; width: 382px; height: 156px;
    background: linear-gradient(180deg, var(--sky-pale) 0%, #9cc3bb 40%, var(--city-grey) 100%);
  }
  .mark-panel { left: 382px; top: 480px; width: 382px; height: 156px; background: var(--ink-panel); }

  .identity { position: absolute; left: 50px; top: 74px; }
  .identity-name {
    font-family: "Quicksand", sans-serif; font-weight: 700;
    font-size: 20px; color: var(--name-teal); letter-spacing: 0.3px;
  }
  .identity-role {
    font-family: "Quicksand", sans-serif; font-weight: 400; font-style: italic;
    font-size: 13.5px; color: var(--role-grey); margin-top: 1px;
  }

  .contact-list { position: absolute; right: 39px; top: 297px; list-style: none; }
  .contact-item {
    display: flex; align-items: center; justify-content: flex-end;
    height: 21px; margin-bottom: 9px;
    font-family: "Quicksand", sans-serif; font-weight: 500;
    font-size: 12px; color: var(--detail-tan);
  }
  .contact-icon {
    width: 21px; height: 21px; margin-left: 12px;
    background: var(--accent-red);
    display: flex; align-items: center; justify-content: center;
  }

  .wordmark {
    position: absolute; left: 32px; top: 26px;
    font-family: "Josefin Sans", sans-serif; color: var(--mark-tan);
    line-height: 1;
  }
  .wordmark-first { font-weight: 400; font-size: 52px; letter-spacing: 1px; }
  .wordmark-title { font-weight: 300; font-size: 16px; margin-left: 4px; letter-spacing: 0.5px; }
  .wordmark-last { display: block; font-weight: 300; font-size: 44px; letter-spacing: 0.5px; margin-top: -2px; }
</style>
</head>
<body>
<main class="stage">
  <section class="card-sheet">
    <div class="panel card-back">
      <header class="identity">
        <h1 class="identity-name">Tobias Wrenfield</h1>
        <p class="identity-role">Cinematographer</p>
      </header>
      <ul class="contact-list">
        <li class="contact-item">tkwrenfield@quillbox.example
          <span class="contact-icon">
            <svg width="13" height="10" viewBox="0 0 13 10"><rect x="0.5" y="0.5" width="12" height="9" fill="none" stroke="var(--icon-ink)" stroke-width="1.4"/><path d="M0.8 0.8 L6.5 5.5 L12.2 0.8" fill="none" stroke="var(--icon-ink)" stroke-width="1.4"/></svg>
          </span>
        </li>
        <li class="contact-item">503.618.2907
          <span class="contact-icon">
            <svg width="12" height="12" viewBox="0 0 24 24"><path fill="var(--icon-ink)" d="M6.6 10.8a15.1 15.1 0 0 0 6.6 6.6l2.2-2.2c.3-.3.7-.4 1-.2 1.1.4 2.3.6 3.6.6.6 0 1 .4 1 1V20c0 .6-.4 1-1 1A17 17 0 0 1 3 4c0-.6.4-1 1-1h3.5c.6 0 1 .4 1 1 0 1.3.2 2.5.6 3.6.1.3 0 .7-.2 1z"/></svg>
          </span>
        </li>
        <li class="contact-item">tobiaswrenfield.example
          <span class="contact-icon">
            <svg width="12" height="12" viewBox="0 0 12 12"><circle cx="6" cy="6" r="5.3" fill="none" stroke="var(--icon-ink)" stroke-width="1.3"/><ellipse cx="6" cy="6" rx="2.3" ry="5.3" fill="none" stroke="var(--icon-ink)" stroke-width="1.1"/><line x1="0.7" y1="6" x2="11.3" y2="6" stroke="var(--icon-ink)" stroke-width="1.1"/></svg>
          </span>
        </li>
      </ul>
    </div>
    <div class="panel hero-photo" role="img" aria-label="Close-up nature photograph in dark green and pale tones"></div>
    <div class="panel skyline-photo" role="img" aria-label="Photograph of a city skyline under a pale teal sky"></div>
    <div class="panel mark-panel">
      <div class="wordmark">
        <span class="wordmark-first">TOBIAS</span><span class="wordmark-title">DP</span>
        <span class="wordmark-last">WRENFIELD</span>
      </div>
    </div>
  </section>
</main>
</body>
</html>
```